Verpackungsetikett für Softeisbecher
Zielgruppe
Wir produzieren Speiseeis, füllen dieses in entsprechende Verpackungseinheiten ab und vermarkten es. Zielgruppe sind alle die, die Eis mögen.
Aufgabenstellung
Das bestehende Etikettendesign (rund 8cm Durchmesser) soll neu überarbeitet werden. Dazu soll es mit unserem neuen Logo (Anhang) versehen werden. Wir freuen uns über fotolose Vorschläge bzw. Design´s mit Foto. Alle Angaben über z.B. Inhaltstoffe, Herstellungdatum, Aufbewahrungtemperatur, Barcode u.s.w.kommen auf ein separates Etikett am Boden des Bechers.Das Erscheinungsbild des Etiketts sollte eine gewisse Neutralität haben, so dass es für die verschiedensten Geschmacksrichtungen verwendet werden kann, sprich ein Etikett für alle Eissorten. Nur der Name der Geschmacksrichtung unterscheidet die Etiketten. Wir verweisen auf einige Link`s ,auf denen man Etikettenbeispiele (z. B. Frischkäse) sieht, die unseren Vorstellungen der Gestaltung entsprechen. Vielen Dank im Voraus

```html
<!DOCTYPE html>
<html lang="de">
<head>
<meta charset="utf-8">
<title>Softeis Etikett – Heidelbeer-Joghurt</title>
<link rel="stylesheet" href="https://fonts.googleapis.com/css2?family=Lobster&family=Overlock:ital,wght@0,900;1,700&family=Open+Sans:wght@600&display=swap">
<style>
  :root{
    --ring-dark:#12367f;
    --ring-mid:#3a78bf;
    --ring-light:#9cc3e5;
    --sky:#c4dbf0;
    --wave-deep:#6fa2d6;
    --wave-soft:#b9d4ee;
    --rule:#1f5aa6;
    --leaf-green:#b3c82a;
    --banner-dark:#86ae2a;
    --banner-light:#c3d22c;
    --script-fill:#a9c4e6;
    --ink:#111111;
    --white:#ffffff;
  }
  html,body{margin:0;padding:0;overflow:hidden;background:var(--white);}
  .label{display:block;width:1200px;height:1200px;}
  .brand-name{font-family:"Overlock",sans-serif;font-weight:900;font-size:74px;fill:var(--leaf-green);}
  .product-title{font-family:"Lobster",cursive;font-weight:400;font-size:200px;fill:var(--script-fill);stroke:var(--white);stroke-width:14px;paint-order:stroke;stroke-linejoin:round;}
  .flavour{font-family:"Overlock",sans-serif;font-style:italic;font-weight:700;font-size:52px;fill:var(--ink);}
  .banner-text{font-family:"Open Sans",sans-serif;font-weight:600;font-size:36px;fill:var(--white);}
</style>
</head>
<body>
<svg class="label" viewBox="0 0 944 944" xmlns="http://www.w3.org/2000/svg">
  <defs>
    <linearGradient id="ring-gradient" x1="0.85" y1="0.08" x2="0.35" y2="0.6">
      <stop offset="0" stop-color="var(--ring-dark)"/>
      <stop offset="0.45" stop-color="var(--ring-mid)"/>
      <stop offset="0.8" stop-color="var(--ring-light)"/>
    </linearGradient>
    <linearGradient id="wave-gradient" x1="0" y1="0" x2="1" y2="0">
      <stop offset="0" stop-color="var(--wave-deep)"/>
      <stop offset="1" stop-color="var(--wave-soft)"/>
    </linearGradient>
    <linearGradient id="banner-gradient" x1="0" y1="1" x2="1" y2="0">
      <stop offset="0" stop-color="var(--banner-dark)"/>
      <stop offset="1" stop-color="var(--banner-light)"/>
    </linearGradient>
    <filter id="title-shadow" x="-10%" y="-20%" width="120%" height="140%">
      <feDropShadow dx="2" dy="4" stdDeviation="4" flood-color="#35629a" flood-opacity="0.35"/>
    </filter>
    <clipPath id="label-face"><circle cx="472" cy="472" r="420"/></clipPath>
    <clipPath id="label-outline"><circle cx="472" cy="472" r="472"/></clipPath>
  </defs>

  <circle class="outer-ring" cx="472" cy="472" r="472" fill="url(#ring-gradient)"/>
  <circle class="ring-rim" cx="472" cy="472" r="426" fill="var(--white)"/>

  <g class="face" clip-path="url(#label-face)">
    <rect x="0" y="0" width="944" height="944" fill="var(--sky)"/>
    <path class="swoosh" d="M40 300 C240 180 520 200 700 230 C800 245 880 220 944 200 L944 560 L40 560 Z" fill="var(--white)"/>
    <path class="wave-back" d="M40 560 C220 520 420 600 600 600 C740 600 860 560 944 520 L944 712 L40 712 Z" fill="var(--wave-soft)"/>
    <path class="wave-front" d="M40 590 C200 570 360 640 560 690 C640 706 720 712 760 712 L40 712 Z" fill="url(#wave-gradient)"/>
    <rect class="rule" x="40" y="709" width="880" height="4" fill="var(--rule)"/>
    <rect class="flavour-field" x="40" y="713" width="880" height="260" fill="var(--white)"/>
  </g>

  <g class="banner" clip-path="url(#label-outline)">
    <rect x="-200" y="90" width="900" height="118" fill="url(#banner-gradient)" transform="rotate(-38 250 150)"/>
    <text class="banner-text" x="250" y="163" text-anchor="middle" transform="rotate(-38 250 150)">Natürlich lecker!</text>
  </g>

  <g class="brand">
    <circle cx="472" cy="225" r="58" fill="var(--ring-light)"/>
    <text class="brand-name" x="472" y="385" text-anchor="middle">Auwiese</text>
  </g>

  <text class="product-title" x="478" y="620" text-anchor="middle" filter="url(#title-shadow)">Softeis</text>

  <text class="flavour" x="478" y="788" text-anchor="middle">Heidelbeer-</text>
  <text class="flavour" x="478" y="845" text-anchor="middle">Joghurt</text>
</svg>
</body>
</html>
```